Classy business card for accounting firm

We're looking for a new business card for our accounting firm. Our logo was designed by Brandolith, so all of the design info we would like to use has been provided. The specific font provided isn't required to be used.

We want the card to look classy and elegent. Probably more minimalistic, but still with some pops of color.

The options we would like to include on the card are as follows:
1. Main office phone line
2. Direct phone line
3. Email address
4. Website URL
5. Name
6. Title (CEO, President, etc.)
7. Firm Address

The design and card should be double sided!!! The drop down box in the project brief for some reason is defaulting to single sided. Not sure why this is happening.

Thanks!

Contact Information for Business Card

The options we would like to include on the card are as follows: 1. Main office phone line 2. Direct phone line 3. Email address 4. Website URL 5. Name 6. Title (CEO, President, etc.) 7. Firm Address

Requirements
Must have
• Card must be double sided.

```html
<!DOCTYPE html>
<html lang="en">
<head>
<meta charset="utf-8">
<title>Ledgerwell Partners – Business Card</title>
<link rel="stylesheet" href="https://fonts.googleapis.com/css2?family=Montserrat:wght@400;500;600;700&display=swap">
<style>
  :root {
    --backdrop: #e6e6e6;
    --card-white: #f7f7f7;
    --ink-grey: #555759;
    --leaf-dark: #949f25;
    --leaf-light: #b3bb3c;
    --leaf-line: #a8b52c;
    --accent-orange: #e87722;
    --text-light: #f4f6e4;
  }
  * { margin: 0; padding: 0; box-sizing: border-box; }
  html, body {
    width: 1200px; height: 1200px; overflow: hidden;
    background: var(--backdrop);
    font-family: "Montserrat", sans-serif;
  }
  .canvas { position: relative; width: 1200px; height: 1200px; }
  .card { position: absolute; left: 234px; width: 731px; height: 416px; }
  .card-front { top: 160px; background: var(--card-white); }
  .card-back {
    top: 631px;
    background: linear-gradient(110deg, var(--leaf-dark) 0%, var(--leaf-light) 100%);
  }

  /* Front */
  .front-square {
    position: absolute; left: 345px; top: 128px;
    width: 40px; height: 40px; background: var(--accent-orange);
  }
  .front-name {
    position: absolute; left: 0; right: 0; top: 238px; text-align: center;
    font-size: 31px; font-weight: 600; letter-spacing: 1.5px; line-height: 1;
    color: var(--ink-grey); text-transform: uppercase; white-space: nowrap;
  }
  .front-tagline {
    position: absolute; left: 146px; width: 441px; top: 286px;
    display: flex; align-items: center; gap: 16px;
    font-size: 16px; font-weight: 600; letter-spacing: 3px; line-height: 1;
    color: var(--ink-grey); text-transform: uppercase; white-space: nowrap;
  }
  .front-tagline::before, .front-tagline::after {
    content: ""; flex: 1; height: 2px; background: var(--leaf-line);
  }

  /* Back */
  .back-square {
    position: absolute; left: 152px; top: 40px;
    width: 24px; height: 24px; background: var(--accent-orange);
  }
  .back-brand { position: absolute; left: 52px; top: 100px; width: 224px; }
  .back-name {
    text-align: center; font-size: 16.5px; font-weight: 600; letter-spacing: 0.3px;
    line-height: 1; color: var(--ink-grey); text-transform: uppercase; white-space: nowrap;
  }
  .back-tagline {
    margin-top: 8px; display: flex; align-items: center; gap: 7px;
    font-size: 8.5px; font-weight: 600; letter-spacing: 1.2px; line-height: 1;
    color: var(--ink-grey); text-transform: uppercase; white-space: nowrap;
  }
  .back-tagline::before, .back-tagline::after {
    content: ""; flex: 1; height: 1px; background: var(--text-light);
  }
  .person { position: absolute; left: 406px; top: 120px; color: #fff; }
  .person-name { font-size: 28px; font-weight: 700; line-height: 1.1; }
  .person-title { margin-top: 6px; font-size: 17px; font-weight: 400; color: var(--text-light); }
  .divider {
    position: absolute; left: 407px; right: 0; top: 199px;
    height: 2px; background: var(--text-light);
  }
  .contacts { position: absolute; left: 403px; top: 220px; list-style: none; }
  .contacts li {
    display: flex; align-items: center; height: 28.5px;
    font-size: 17px; color: var(--text-light);
  }
  .contacts svg { width: 16px; height: 16px; margin-right: 10px; fill: var(--text-light); }
  .address {
    position: absolute; left: 0; right: 0; top: 358px; text-align: center;
    font-size: 17px; color: var(--text-light);
  }
</style>
</head>
<body>
<div class="canvas">
  <section class="card card-front">
    <span class="front-square"></span>
    <p class="front-name">Ledgerwell Partners</p>
    <p class="front-tagline">Balanced Tax Advice</p>
  </section>

  <section class="card card-back">
    <span class="back-square"></span>
    <div class="back-brand">
      <p class="back-name">Ledgerwell Partners</p>
      <p class="back-tagline">Balanced Tax Advice</p>
    </div>

    <div class="person">
      <p class="person-name">Marlow Pennick</p>
      <p class="person-title">President</p>
    </div>
    <div class="divider"></div>

    <ul class="contacts">
      <li>
        <svg viewBox="0 0 16 16" aria-hidden="true"><path d="M3.6 1.2l2.3 2.6-1.3 1.8c.9 2 2.6 3.7 4.6 4.7l1.8-1.3 2.6 2.3-1.5 2.6C6.9 13.4 2.6 9.1 1.1 2.9z"/></svg>
        555-014-2280
      </li>
      <li>
        <svg viewBox="0 0 16 16" aria-hidden="true"><path d="M4.5 0h7A1.5 1.5 0 0 1 13 1.5v13a1.5 1.5 0 0 1-1.5 1.5h-7A1.5 1.5 0 0 1 3 14.5v-13A1.5 1.5 0 0 1 4.5 0zM4.5 2v10.5h7V2zM8 13.3a.9.9 0 1 0 0 1.8.9.9 0 0 0 0-1.8z"/></svg>
        555-019-7361
      </li>
      <li>
        <svg viewBox="0 0 16 16" aria-hidden="true"><path d="M1 3h14v1.2L8 9 1 4.2zM1 5.8l7 4.8 7-4.8V13H1z"/></svg>
        info@LedgerwellPartners.com
      </li>
      <li>
        <svg viewBox="0 0 16 16" aria-hidden="true"><path d="M8 0a8 8 0 1 0 0 16A8 8 0 0 0 8 0zM7 1.2V7H4.1C4.3 4.4 5.4 2.2 7 1.2zm2 0c1.6 1 2.7 3.2 2.9 5.8H9zM1.3 9h1.8c.1 2 .7 3.8 1.6 5A6.9 6.9 0 0 1 1.3 9zM7 9v5.8C5.4 13.8 4.3 11.6 4.1 9zm2 0h2.9c-.2 2.6-1.3 4.8-2.9 5.8zm3.9 0h1.8a6.9 6.9 0 0 1-3.4 5c.9-1.2 1.5-3 1.6-5zM1.3 7a6.9 6.9 0 0 1 3.4-5C3.8 3.2 3.2 5 3.1 7zm11.6 0c-.1-2-.7-3.8-1.6-5a6.9 6.9 0 0 1 3.4 5z"/></svg>
        www.LedgerwellPartners.com
      </li>
    </ul>

    <p class="address">4870 Alder Crest Lane Fairhaven Maine 04120</p>
  </section>
</div>
</body>
</html>
```